Lumigram Page Design for a Medical Billing Business

We need help designing a lumigram page that is professional, yet friendly that will attract medical practitioners (doctors, therapists, nutritionists, chiropractors, etc) to check out and follow our business. I have attached our logo which must be incorporated in the design.

```html
<!DOCTYPE html>
<html lang="en">
<head>
<meta charset="utf-8">
<title>Vessa Medical Billing – Lumigram Cover</title>
<link rel="stylesheet" href="https://fonts.googleapis.com/css2?family=Montserrat:ital,wght@0,500;0,600;1,800&display=swap">
<style>
  :root {
    --page-bg: #e6e6e6;
    --lavender: #a88ad8;
    --periwinkle: #7f8fd6;
    --teal: #2ea3bd;
    --deep-teal: #0f5d70;
    --ink: #000000;
    --text-light: #ffffff;
    --brand: #b48ad8;
  }
  * { box-sizing: border-box; margin: 0; padding: 0; }
  html, body {
    width: 1200px;
    height: 1200px;
    overflow: hidden;
    background: var(--page-bg);
  }
  .cover {
    position: absolute;
    left: 38px;
    top: 354px;
    width: 1124px;
    height: 492px;
    overflow: hidden;
    font-family: "Montserrat", sans-serif;
    color: var(--text-light);
  }
  .cover__photo {
    position: absolute;
    inset: 0;
    background:
      radial-gradient(ellipse at 95% 100%, var(--ink) 0%, rgba(0,0,0,0.9) 25%, rgba(0,0,0,0) 60%),
      linear-gradient(100deg, var(--lavender) 0%, var(--periwinkle) 28%, var(--teal) 52%, var(--deep-teal) 72%, var(--ink) 90%);
  }
  .cover__headline {
    position: absolute;
    left: 124px;
    top: 28px;
    font-size: 72px;
    font-weight: 800;
    font-style: italic;
    line-height: 76px;
    letter-spacing: -0.5px;
  }
  .cover__pitch {
    position: absolute;
    left: 124px;
    top: 232px;
    font-size: 29px;
    font-weight: 500;
    line-height: 48px;
  }
  .cover__brand {
    position: absolute;
    left: 770px;
    top: 346px;
    display: flex;
    align-items: center;
    gap: 12px;
    font-size: 30px;
    font-weight: 600;
    color: var(--brand);
  }
  .cover__brand-dot {
    width: 14px;
    height: 14px;
    border-radius: 50%;
    background: var(--brand);
  }
</style>
</head>
<body>
  <section class="cover">
    <div class="cover__photo" role="img" aria-label="Photo of a medical practitioner at a desk reviewing billing paperwork, tinted purple to teal fading to black"></div>
    <h1 class="cover__headline">Get your<br>billings right!</h1>
    <p class="cover__pitch">We help medical practitioners<br>to get their business done.<br>Come check us out!</p>
    <div class="cover__brand">
      <span class="cover__brand-dot"></span>
      <span class="cover__brand-name">Vessa Medical Billing</span>
    </div>
  </section>
</body>
</html>
```